Lumorax Helpdesk overview brochure

Take the word document that is attached and turn it into a brochure. (Thinking one page, front and back.) the only existing branding/colors we have is the logo that is on the document. It may require a phone all or a bit of back and forth in text to explain some of the concepts in the attached document.

Target Market(s)

Call centers

Industry/Entity Type

It Service

Font styles to use
Sans Serif

Colors

Designer to choose colors to be used in the design.

Requirements
Must have
• A crisp professional look

```html
<!DOCTYPE html>
<html lang="en">
<head>
<meta charset="utf-8">
<title>Lumorax Helpdesk – Overview Brochure</title>
<link href="https://fonts.googleapis.com/css2?family=Roboto:wght@300;400;500&display=swap" rel="stylesheet">
<style>
:root{
  --blue:#1f9ad6;
  --blue-dark:#2e8cc7;
  --blue-light:#5bbde6;
  --blue-pale:#a3d9ec;
  --band-blue:#7cc3d9;
  --grey-dark:#555659;
  --text:#4a4a4a;
  --paper:#ffffff;
  --paper-grey:#f1f1f1;
  --bg:#e6e4e0;
}
*{margin:0;padding:0;box-sizing:border-box}
html,body{width:1200px;height:857px;overflow:hidden;background:var(--bg)}
body{font-family:'Roboto',Arial,sans-serif;color:var(--text);position:relative}
.page{position:absolute;width:498px;height:645px;background:var(--paper);overflow:hidden;box-shadow:0 4px 14px rgba(0,0,0,.25)}
.page--front{left:74px;top:55px}
.page--back{left:629px;top:130px;background:linear-gradient(#fff 0,#fff 240px,var(--paper-grey) 250px,#fafafa 100%)}
.photo{position:absolute;left:0;top:0;width:498px}
.photo--meeting{height:283px;background:linear-gradient(135deg,#3b2a20 0%,#7a5a44 40%,#a7b9c6 55%,#5b4232 100%)}
.photo--man{height:236px;background:radial-gradient(circle at 70% 45%,#d8b59a 0,#8c6a55 18%,transparent 30%),linear-gradient(90deg,#e9e2d3 0%,#c9b28a 35%,#6d5a48 70%,#3d3029 100%)}
.shapes{position:absolute;left:0;top:0}
.brand{position:absolute;display:flex;align-items:center;gap:6px;font-weight:500;color:#fff;letter-spacing:.3px}
.brand__dot{width:16px;height:16px;border-radius:50%;background:#fff;flex:none}
.brand--cloud{left:186px;top:210px;color:var(--blue);font-size:14px}
.brand--cloud .brand__dot{background:var(--blue)}
.brand--top{left:18px;top:34px;font-size:14px}
.badge-circle{position:absolute;border-radius:50%;border:3px solid #fff;background:rgba(255,255,255,.15)}
.headline{position:absolute;left:10px;width:478px;top:306px;text-align:center;color:var(--blue);font-size:12.4px;font-weight:300;line-height:16.5px;white-space:nowrap}
.body-copy{position:absolute;left:21px;top:352px;width:277px;font-size:8.6px;line-height:9.8px;text-align:justify;font-weight:300;color:#333}
.body-copy p{margin-bottom:9px}
.channel-icons{position:absolute;left:24px;top:567px;display:flex;gap:8px;align-items:center}
.channel-icons span{width:16px;height:16px;display:block}
.costs-card{position:absolute;left:323px;top:378px;width:146px;height:184px;background:var(--blue-pale);text-align:center}
.costs-card::after{content:"";position:absolute;left:62px;bottom:-13px;border-left:11px solid transparent;border-right:11px solid transparent;border-top:13px solid var(--blue-pale)}
.costs-card__bubble{position:absolute;left:46px;top:-22px;width:54px;height:54px;border-radius:50%;background:var(--blue-pale);display:flex;align-items:center;justify-content:center}
.costs-card__bubble i{width:40px;height:40px;border-radius:50%;background:#fff;display:flex;align-items:center;justify-content:center}
.costs-card__title{position:absolute;top:44px;width:100%;font-size:9.6px;letter-spacing:.6px;line-height:16px;color:#4b5d66}
.costs-card__rule{position:absolute;left:12px;right:12px;top:82px;border-top:1px solid #fff}
.cost{position:absolute;left:8px;display:flex;gap:6px;text-align:left;color:#3b6e86}
.cost b{font-weight:400;font-size:8.2px;display:block;line-height:11px;letter-spacing:-.2px}
.cost small{font-size:6.6px;display:block;line-height:10px}
.contact{position:absolute;right:20px;text-align:right;color:#fff;font-size:10px;line-height:15px;font-weight:300}
.contact li{list-style:none;display:flex;justify-content:flex-end;align-items:center;gap:6px}
.contact li i{width:9px;height:9px;background:var(--blue);display:inline-block}
.section-bar{position:absolute;left:0;top:256px;width:240px;height:23px;background:var(--band-blue);color:#3c4d55;font-size:11px;padding:5px 16px;letter-spacing:.2px}
.col{position:absolute;font-size:8.6px;line-height:11.6px;color:#444;font-weight:300}
.col h3{color:var(--blue);font-weight:400;font-size:9.6px;margin-bottom:4px}
.col p{margin-bottom:14px}
.col ul{list-style:none}
.col li{line-height:13px}
.col--left{left:16px;top:296px;width:208px}
.col--right{left:260px;top:270px;width:212px}
.photo--phone{position:absolute;left:246px;top:456px;width:119px;height:134px;border-radius:16px 16px 4px 4px;background:linear-gradient(160deg,#1b1b1d 0%,#3d4b57 40%,#9aa9b5 60%,#d7b59d 85%,#c59a80 100%)}
</style>
</head>
<body>

<section class="page page--front">
  <div class="photo photo--meeting" role="img" aria-label="Top-down photo of business team holding paper clouds joined by lines around a central cloud"></div>
  <svg class="shapes" width="498" height="420" viewBox="0 0 498 420">
    <polygon points="236,283 498,190 498,283" fill="var(--blue-dark)"/>
    <polygon points="300,283 498,232 498,300" fill="var(--blue-light)"/>
    <polygon points="380,283 498,262 498,334" fill="var(--blue)"/>
  </svg>
  <div class="brand brand--cloud"><span class="brand__dot"></span>Lumorax Helpdesk</div>
  <div class="badge-circle" style="left:410px;top:226px;width:46px;height:46px"></div>

  <h2 class="headline">Lumorax Helpdesk helps contact centers serve new customer<br>access channels, improve customer service, and lower costs of operation.</h2>

  <div class="body-copy">
    <p>The huge popularity of social media and messaging is creating customer preferences to communicate with your company using SMS text messaging, Chatterly Messenger, Teamloop, Vocaly, Homevoice, Hubnest home, and many other new channels.</p>
    <p>App fatigue has set in. Customers are weary of installing, updating and learning how to use mobile apps. Your customers want to communicate with you using their messaging service of choice or just talk into their smart phone, computer, Homevoice or similar device.</p>
    <p>Sensible automation of customer interactions on these new channels can provide better service at even lower costs of operation.</p>
    <p>According to Veridex Research's report, by 2020, 85% of customer interactions will be managed without a human.</p>
    <p>Using specific techniques, Lumorax Helpdesk will help you shift some traffic from higher cost telephone calls to lower cost messaging channels. Shaping your traffic into lower cost channels has great financial benefits.</p>
  </div>

  <div class="channel-icons" aria-hidden="true">
    <span style="background:#1f8fd6;border-radius:3px"></span>
    <span style="background:#3bb34a;border-radius:3px"></span>
    <span style="background:#2fb54a;border-radius:3px"></span>
    <span style="background:#8dc63f;border-radius:3px"></span>
    <span style="background:#3a7fe0;border-radius:50%"></span>
    <span style="background:#6d6e71;border-radius:50%"></span>
    <span style="background:#e0457b;border-radius:3px"></span>
    <span style="background:#f2a23a;border-radius:3px"></span>
  </div>

  <div class="costs-card">
    <div class="costs-card__bubble"><i>
      <svg width="22" height="18" viewBox="0 0 22 18"><path d="M2 2h13v8H7l-4 3v-3H2z" fill="#555"/><path d="M17 6h3v8h-1v3l-3-3h-6v-2h7z" fill="#888"/></svg>
    </i></div>
    <div class="costs-card__title">EXISTING CHANNELS<br>HAVE DIFFERENT COSTS</div>
    <div class="costs-card__rule"></div>
    <div class="cost" style="top:95px">
      <svg width="10" height="10" viewBox="0 0 10 10"><rect x="0.5" y="1.5" width="8" height="8" fill="none" stroke="#3b6e86"/><path d="M2 5l2 2 5-6" fill="none" stroke="#3b6e86" stroke-width="1.2"/></svg>
      <div><b>Telephone call with a live agent</b><small>Average cost per call is $17 *</small></div>
    </div>
    <div class="cost" style="top:128px">
      <svg width="10" height="10" viewBox="0 0 10 10"><rect x="0.5" y="1.5" width="8" height="8" fill="none" stroke="#3b6e86"/><path d="M2 5l2 2 5-6" fill="none" stroke="#3b6e86" stroke-width="1.2"/></svg>
      <div><b>Webchat with a live agent</b><small>Average cost per web chat is $12*</small></div>
    </div>
  </div>

  <svg class="shapes" style="top:570px" width="498" height="75" viewBox="0 0 498 75">
    <polygon points="0,17 360,75 0,75" fill="var(--blue)"/>
    <polygon points="498,2 498,75 190,75" fill="var(--grey-dark)"/>
  </svg>
  <ul class="contact" style="top:596px">
    <li>555-014-2290 <i></i></li>
    <li>hello@lumoraxhelpdesk.com <i></i></li>
    <li>www.lumoraxsolutions.net <i></i></li>
  </ul>
</section>

<section class="page page--back">
  <div class="photo photo--man" role="img" aria-label="Photo of a smiling businessman looking at his smartphone against blurred city lights"></div>
  <svg class="shapes" width="498" height="240" viewBox="0 0 498 240">
    <polygon points="0,0 258,0 0,122" fill="var(--blue)"/>
    <polygon points="0,60 216,45 0,150" fill="var(--blue-light)" opacity=".85"/>
  </svg>
  <div class="brand brand--top"><span class="brand__dot"></span>Lumorax Helpdesk</div>

  <div class="section-bar">ENGAGEMENT MODEL</div>

  <div class="col col--left">
    <h3>PROPOSAL</h3>
    <p>Lumorax Helpdesk provides a written proposal. The proposal will describe our engagement methodologies and costs.</p>
    <h3>ENGAGEMENT</h3>
    <p style="margin-bottom:3px">Lumorax Helpdesk will meet with all the relevant stake holders on site and gather information to identify:</p>
    <ul>
      <li>• Historical traffic patterns</li>
      <li>• Actual costs by channel</li>
      <li>• Review marketing plans that may impact customer service</li>
      <li>• Review product plans that may impact customer service.</li>
      <li>• Explore competition landscape as it relates to customer service.</li>
      <li>• Review the existing corporate data store, analytics and reporting</li>
      <li>• Review the current plans, metrics and budgets for customer service support</li>
    </ul>
  </div>

  <div class="col col--right">
    <h3>TRANSFORMATION REPORT</h3>
    <ul>
      <li>• Executive summary</li>
      <li>• Cost analysis per contact by channel</li>
      <li>• Traffic patterns by channel</li>
      <li>• Probable impacts of product and marketing plans</li>
      <li>• Recommendations for achieving competitive advantage through service</li>
      <li>• Recommendations for new channel types</li>
      <li>• Recommendations for traffic shaping</li>
      <li>• Near and long-term options for sensible automation</li>
      <li>• Technology recommendations for implementing new channels</li>
      <li>• Projected financial impact of recommendations</li>
    </ul>
  </div>

  <div class="photo--phone" role="img" aria-label="Photo of a hand holding a smartphone showing a finger touching a cloud icon"></div>
  <div class="badge-circle" style="left:395px;top:500px;width:56px;height:56px;border-color:var(--grey-dark);background:none"></div>

  <svg class="shapes" style="top:570px" width="498" height="75" viewBox="0 0 498 75">
    <polygon points="0,17 300,75 0,75" fill="var(--blue)"/>
    <polygon points="498,10 498,75 185,75" fill="var(--grey-dark)"/>
  </svg>
  <ul class="contact" style="top:596px">
    <li>555-014-2290 <i></i></li>
    <li>hello@lumoraxhelpdesk.com <i></i></li>
    <li>www.lumoraxsolutions.net <i></i></li>
  </ul>
</section>

</body>
</html>
```